Business Card Design for Quorvane

Need a business card designed for Quorvane employees.
- 2 sided business card
- Front:
Company Logo (file attached)
Background could be:white with perhaps a red/black stripe on the left
OR
Background could be: OR dark red-black gradient: be creative
Include the following on the front:
Martin Delacroy
Founder & CEO
martin.delacroy@quorvane-example.com
+1 555.013.4782
quorvane-example.com
- Back: White color background with company logo
Text under the logo: Invoice Automation 2.0
** be creative about the font, mix of upper and lower case and colors for the text **
Target Market(s)
We are a software company marketing our products to large and medium sized businesses.
Industry/Entity Type
Business

```html
<!DOCTYPE html>
<html lang="en">
<head>
<meta charset="utf-8">
<title>Quorvane Business Card</title>
<link rel="stylesheet" href="https://fonts.googleapis.com/css2?family=Ubuntu:wght@300;400;500&display=swap">
<style>
  :root {
    --page-bg: #e3e1de;
    --card-bg: #f3f3f3;
    --ink: #2b2b2b;
    --ink-soft: #4a4a4a;
    --accent-red: #8c1c1c;
    --accent-orange: #c4561a;
    --card-shadow: 0 10px 28px rgba(0, 0, 0, 0.18);
  }
  * { box-sizing: border-box; margin: 0; padding: 0; }
  html, body {
    width: 1200px;
    height: 900px;
    overflow: hidden;
    background: var(--page-bg);
    font-family: "Ubuntu", sans-serif;
    color: var(--ink);
  }
  .sheet {
    width: 1200px;
    height: 900px;
    display: flex;
    flex-direction: column;
    align-items: center;
    justify-content: center;
    gap: 40px;
  }
  .card {
    position: relative;
    width: 630px;
    height: 360px;
    background: var(--card-bg);
    box-shadow: var(--card-shadow);
  }
  .brand {
    display: flex;
    align-items: center;
    gap: 18px;
  }
  .brand-dot {
    width: 64px;
    height: 64px;
    border-radius: 50%;
    background: var(--accent-orange);
    flex: none;
  }
  .brand-name {
    font-weight: 400;
    font-size: 50px;
    letter-spacing: 6px;
    text-transform: uppercase;
    color: var(--ink);
    line-height: 1;
  }

  /* Back side */
  .card-back {
    display: flex;
    flex-direction: column;
    align-items: center;
    justify-content: center;
  }
  .tagline {
    margin-top: 14px;
    margin-left: 82px;
    font-weight: 300;
    font-size: 19px;
    letter-spacing: 4px;
    text-transform: uppercase;
    color: var(--ink-soft);
  }
  .tagline-version { color: var(--accent-red); }

  /* Front side */
  .card-front .brand {
    position: absolute;
    left: 58px;
    top: 92px;
  }
  .person {
    position: absolute;
    left: 58px;
    bottom: 62px;
  }
  .person-name {
    font-weight: 400;
    font-size: 25px;
    letter-spacing: 1.5px;
    text-transform: uppercase;
    color: var(--ink);
  }
  .person-role {
    margin-top: 4px;
    font-weight: 400;
    font-size: 17px;
    color: var(--ink-soft);
  }
  .contact {
    position: absolute;
    left: 336px;
    top: 196px;
    padding-left: 16px;
    border-left: 1.5px solid var(--accent-red);
    font-weight: 300;
    font-size: 12.5px;
    line-height: 1.65;
    color: var(--ink-soft);
  }
  .contact-web { color: var(--accent-red); font-weight: 400; }
</style>
</head>
<body>
  <main class="sheet">
    <section class="card card-back" aria-label="Card back">
      <div class="brand">
        <span class="brand-dot"></span>
        <span class="brand-name">Quorvane</span>
      </div>
      <p class="tagline">Invoice Automation <span class="tagline-version">2.0</span></p>
    </section>

    <section class="card card-front" aria-label="Card front">
      <div class="brand">
        <span class="brand-dot"></span>
        <span class="brand-name">Quorvane</span>
      </div>
      <div class="person">
        <p class="person-name">Martin Delacroy</p>
        <p class="person-role">Founder &amp; CEO</p>
      </div>
      <div class="contact">
        <p class="contact-email">martin.delacroy@quorvane-example.com</p>
        <p class="contact-phone">+1 555.013.4782</p>
        <p class="contact-web">quorvane-example.com</p>
      </div>
    </section>
  </main>
</body>
</html>
```